Paleo Diet Book Cover Design

I need a cover designed for my book Stone Frame that will be sold on Brightleaf Reader and other sites. So the front, side and back will need to be designed. I have attached part of the book here so feel free to skim through the content and give it a quick read to get a feel for what the book is about. Stone Frame is about eating the diet of the caveman (paleolithic era-paleo) and a 12 week workout plan with a grocery shopping list and meal plans. It is for men and women ages 18+ who are interested in health and fitness and becoming healthier overall.
The graphics should be secondary, and it should add to the text, not distract from it. This is even more important because the size of the cover displayed on Brightleaf/Reader, when your book is first seen by a potential buyer, is so tiny. It's barely an inch high, and even smaller in width.
So the words have to be big, bold, benefit-rich and easy to read. That also means, don't mess with the fancy fonts. Clean, clear, crisp font is best. And, did I say BIG already?
Contrast the colors of the text and background, so its even easier to read. That means, dark text on light background or visa versa. Colors like darker reds, blues / teals and oranges.
Please read this: http://www.jacketforge.net/8-cover-design-secrets-publishers-use-to-manipulate-readers-into-buying-books/
The cover has to be bold and easy to read, it has to stick out, it has to draw the attention of your readers so that they zero in on my book, out of all the other books on the page. (Much like they would when viewing a classified ads site/page.)
The Title of the Book is Stone Frame, and the subtitle is "Transform Your Body For Life in 12 Weeks With Proven Workouts and Paleo Diet Based Nutrition" Perhaps “Transform Your Body For Life in 12 Weeks” could also be in a large font similar to the title with the rest of the subtitle following afterwards. You can try having the title be the smaller font with the subtitle being the larger font as well.
Then the authors name "Martin Oakes” incorporated into the design.
I am not sure what to use as the background type of design for the front of the book so feel free to be creative with that.
The size needs to be 1563 pixels on the shortest side and 2500 pixels on the longest side just for the front of the cover.

```html
<!DOCTYPE html>
<html lang="en">
<head>
<meta charset="utf-8">
<title>Stone Frame – Book Cover</title>
<link rel="stylesheet" href="https://fonts.googleapis.com/css2?family=Bebas+Neue&family=Roboto+Condensed:wght@400;700&display=swap">
<style>
  :root {
    --stage: #e9e9e7;
    --paper: #ffffff;
    --orange: #f04e0f;
    --green: #84c51a;
    --green-band: #8bc91c;
    --white: #ffffff;
    --skin-light: #f4e3d6;
    --skin-mid: #e8cbb6;
  }
  * { margin: 0; padding: 0; box-sizing: border-box; }
  html, body {
    width: 1200px; height: 808px; overflow: hidden;
    background: var(--stage);
  }
  .cover {
    position: absolute; left: 345px; top: 0;
    width: 510px; height: 808px;
    background: var(--paper);
    overflow: hidden;
    font-family: "Roboto Condensed", "Arial Narrow", sans-serif;
  }
  .cover-photo {
    position: absolute; left: 300px; top: 0; width: 210px; height: 598px;
    background: linear-gradient(100deg, var(--paper) 0%, var(--skin-light) 35%, var(--skin-mid) 70%, var(--skin-light) 100%);
  }
  .title-band {
    position: absolute; left: 0; top: 20px; width: 352px; height: 160px;
    background: var(--orange);
  }
  .title {
    position: absolute; left: 30px;
    font-family: "Bebas Neue", "Oswald", sans-serif;
    line-height: 1; letter-spacing: 2px;
  }
  .title-top { top: 22px; font-size: 166px; color: var(--white); }
  .title-bottom { top: 180px; font-size: 166px; color: var(--green); }
  .promise {
    position: absolute; left: 40px; font-weight: 700;
    font-size: 54px; line-height: 1; letter-spacing: 0.5px;
  }
  .promise-1 { top: 349px; color: var(--green); }
  .promise-2 { top: 408px; color: var(--orange); }
  .promise-3 { top: 468px; color: var(--green); }
  .weeks-badge {
    position: absolute; left: 238px; top: 458px; width: 116px; height: 118px;
  }
  .weeks-badge svg { position: absolute; left: 0; top: 0; }
  .weeks-label {
    position: absolute; color: var(--white); font-weight: 700; line-height: 1;
  }
  .weeks-in { left: 12px; top: 30px; font-size: 20px; writing-mode: vertical-rl; transform: rotate(180deg); }
  .weeks-num { left: 34px; top: 14px; font-size: 66px; letter-spacing: -2px; }
  .weeks-word { left: 14px; top: 80px; font-size: 30px; }
  .benefit-band {
    position: absolute; left: 0; top: 598px; width: 510px; height: 154px;
    background: var(--green-band); color: var(--white);
    font-size: 39px; line-height: 46px; text-align: center;
    padding-top: 30px;
  }
  .benefit-band strong { font-weight: 700; }
  .author {
    position: absolute; left: 0; top: 764px; width: 510px; text-align: center;
    color: var(--orange); font-size: 33px; line-height: 1;
  }
  .author strong { font-weight: 700; }
</style>
</head>
<body>
  <main class="cover">
    <div class="cover-photo" role="img" aria-label="Photo of a fit woman's waist with a measuring tape, giving a thumbs up"></div>

    <div class="title-band"></div>
    <h1>
      <span class="title title-top">STONE</span>
      <span class="title title-bottom">FRAME</span>
    </h1>

    <p class="promise promise-1">TRANSFORM</p>
    <p class="promise promise-2">YOUR BODY</p>
    <p class="promise promise-3">FOR LIFE</p>

    <div class="weeks-badge">
      <svg width="130" height="132" viewBox="0 0 130 132" aria-hidden="true">
        <rect x="12" y="12" width="114" height="116" rx="4" fill="none" stroke="#f04e0f" stroke-width="1.5"/>
        <rect x="6" y="6" width="114" height="116" rx="4" fill="#ffffff" stroke="#f04e0f" stroke-width="1.5"/>
        <rect x="0" y="0" width="114" height="116" rx="4" fill="#f04e0f"/>
      </svg>
      <span class="weeks-label weeks-in">IN</span>
      <span class="weeks-label weeks-num">12</span>
      <span class="weeks-label weeks-word">WEEKS</span>
    </div>

    <div class="benefit-band">
      <p>With <strong>Proven Workouts</strong> and</p>
      <p><strong>Paleo Diet Based</strong> Nutrition</p>
    </div>

    <p class="author">Martin <strong>Oakes</strong></p>
  </main>
</body>
</html>
```